Keystone Ward Security - Trade Show Booth 10x20

I need designs for an upcoming trade show booth. We want something sleek, simple that represents our brand well.

Target Market(s)

property Managers

```html
<!DOCTYPE html>
<html lang="en">
<head>
<meta charset="utf-8">
<title>Keystone Ward Security – Trade Show Booth</title>
<link href="https://fonts.googleapis.com/css2?family=Exo+2:wght@500;600;700&display=swap" rel="stylesheet">
<style>
  :root {
    --red: #d8392f;
    --navy: #1c3a4e;
    --ink: #1f3547;
    --paper: #ffffff;
    --stage: #eeeeee;
    --night-1: #1a0f10;
    --night-2: #2b1a1c;
    --night-3: #123a44;
  }
  html, body {
    margin: 0;
    width: 1040px;
    height: 1200px;
    overflow: hidden;
    background: var(--stage);
  }
  .booth-graphic {
    position: absolute;
    left: 40px;
    top: 360px;
    width: 960px;
    height: 480px;
    box-shadow: 0 18px 40px rgba(0,0,0,0.18);
  }
  .brand-name {
    font-family: "Exo 2", sans-serif;
    font-weight: 700;
    fill: var(--paper);
  }
  .services-title {
    font-family: "Exo 2", sans-serif;
    font-weight: 700;
    fill: var(--red);
  }
  .service-label {
    font-family: "Exo 2", sans-serif;
    font-weight: 600;
    font-size: 17px;
    fill: var(--ink);
  }
  .contact-phone {
    font-family: "Exo 2", sans-serif;
    font-weight: 600;
    font-size: 52px;
    fill: var(--ink);
  }
  .contact-web {
    font-family: "Exo 2", sans-serif;
    font-weight: 600;
    font-size: 30px;
    fill: var(--ink);
  }
</style>
</head>
<body>
<svg class="booth-graphic" viewBox="0 0 1396 698" xmlns="http://www.w3.org/2000/svg">
  <defs>
    <linearGradient id="nightScene" x1="0" y1="0" x2="1" y2="0.3">
      <stop offset="0" stop-color="var(--night-2)"/>
      <stop offset="0.45" stop-color="var(--night-3)"/>
      <stop offset="1" stop-color="var(--night-1)"/>
    </linearGradient>
    <g id="tick">
      <rect x="0" y="6" width="28" height="28" rx="4" fill="var(--red)"/>
      <path d="M6 19 L13 27 L30 2" fill="none" stroke="var(--paper)" stroke-width="5" stroke-linecap="round" stroke-linejoin="round"/>
      <path d="M6 19 L13 27 L30 2" fill="none" stroke="var(--red)" stroke-width="2" stroke-linecap="round" stroke-linejoin="round" transform="translate(1.5,-1.5)"/>
    </g>
  </defs>

  <rect class="panel-base" x="0" y="0" width="1396" height="698" fill="var(--paper)"/>

  <polygon class="hero-photo" role="img" aria-label="Night photo of a security officer near a building with a branded patrol vehicle"
    points="0,0 1396,0 1396,323 663,323 330,443 0,328" fill="url(#nightScene)"/>

  <polygon class="chevron-band" points="0,328 330,443 663,323 1396,323 1396,372 663,372 330,505 0,372" fill="var(--red)"/>

  <rect class="footer-band" x="0" y="650" width="1396" height="48" fill="var(--navy)"/>

  <g class="brand">
    <rect x="308" y="100" width="40" height="40" fill="var(--paper)"/>
    <text class="brand-name" x="328" y="240" font-size="44" text-anchor="middle">KEYSTONE WARD</text>
    <text class="brand-name" x="328" y="290" font-size="44" text-anchor="middle">SECURITY</text>
  </g>

  <g class="contact">
    <path d="M102 540 q-6 0 -6 8 q0 20 20 26 q8 2 10 -4 l-8 -5 q-3 4 -6 1 q-5 -5 -6 -12 q0 -3 4 -4 z" fill="var(--red)"/>
    <text class="contact-phone" x="150" y="572">555-214-0987</text>
    <path d="M100 594 L124 604 L114 608 L122 620 L118 622 L110 611 L104 618 Z" fill="var(--red)"/>
    <text class="contact-web" x="150" y="616" textLength="390" lengthAdjust="spacingAndGlyphs">keystonewardsecurity.com</text>
  </g>

  <text class="services-title" x="916" y="452" font-size="54" text-anchor="middle">SERVICES</text>

  <g class="service-list">
    <use href="#tick" x="590" y="490"/>
    <text class="service-label" x="637" y="510"><tspan x="637">SECURITY</tspan><tspan x="637" dy="20">GUARDS</tspan></text>

    <use href="#tick" x="770" y="490"/>
    <text class="service-label" x="812" y="510"><tspan x="812">MOBILE</tspan><tspan x="812" dy="20">PATROL</tspan></text>

    <use href="#tick" x="945" y="490"/>
    <text class="service-label" x="987" y="510"><tspan x="987">INTEGRATED</tspan><tspan x="987" dy="20">SECURITY</tspan><tspan x="987" dy="20">SYSTEMS</tspan></text>

    <use href="#tick" x="1122" y="490"/>
    <text class="service-label" x="1162" y="510"><tspan x="1162">EVENT</tspan><tspan x="1162" dy="20">STAFF</tspan></text>

    <use href="#tick" x="590" y="578"/>
    <text class="service-label" x="637" y="598"><tspan x="637">EMERGENCY</tspan><tspan x="637" dy="20">RESPONSE</tspan></text>

    <use href="#tick" x="770" y="578"/>
    <text class="service-label" x="812" y="598"><tspan x="812">EXECUTIVE</tspan><tspan x="812" dy="20">PROTECTION</tspan></text>

    <use href="#tick" x="945" y="578"/>
    <text class="service-label" x="987" y="598"><tspan x="987">FIRE</tspan><tspan x="987" dy="20">WATCH</tspan></text>

    <use href="#tick" x="1122" y="578"/>
    <text class="service-label" x="1162" y="598"><tspan x="1162">PRIVATE</tspan><tspan x="1162" dy="20">INVESTIGATIONS</tspan></text>
  </g>
</svg>
</body>
</html>
```